Harbor Wick Co Banner Ad for Upcoming holidays

We would like for you to design an ad for Memorial day and Father's Day. For Memorial Day the sale will be 25% OFF select candles and free shipping when you order $50 or more.
For father's day the deal will be get 30% off all candles and free shipping when you order $75 or more.
Please note: These banners will be on our website, they do not require our logo.Banner size: 314 height x 783 width

Industry/Entity Type

Shipping

Requirements
Must have
• Banner size: 314 height x 783 width
Nice to have
• Picture of our unforgettable candle
Should not have
• Logo

```html
<!DOCTYPE html>
<html lang="en">
<head>
<meta charset="utf-8">
<title>Harbor Wick Co – Holiday Banners</title>
<link rel="stylesheet" href="https://fonts.googleapis.com/css2?family=Roboto+Slab:wght@700&family=Tinos:wght@400;700&family=Arimo:wght@400;700&family=Roboto+Condensed:wght@700&family=Dancing+Script:wght@700&display=swap">
<style>
  :root {
    --page: #e9e9e9;
    --navy: #1b2f86;
    --royal: #2a49b8;
    --glow: #6f9ae8;
    --title-light: #e4f0ff;
    --title-mid: #9cc4f2;
    --tag-red: #ec3a35;
    --flag-red: #c42a33;
    --flag-blue: #1e2d73;
    --candle-gold: #e39a2a;
    --sky-top: #7fb8e6;
    --sky-bottom: #eef6fc;
    --band-light: #3d7fd0;
    --band-dark: #1f4aa6;
    --pennant-edge: #7cc8c9;
    --happy-red: #e3283b;
    --fathers-blue: #2a9ad2;
    --day-green: #86b864;
    --text-blue: #1a63b8;
    --sale-pink: #e8246a;
    --wax-red: #a3140f;
    --white: #ffffff;
  }
  * { box-sizing: border-box; margin: 0; padding: 0; }
  html, body {
    width: 1200px; height: 1183px; overflow: hidden;
    background: var(--page);
  }
  .canvas { position: relative; width: 1200px; height: 1183px; }

  .banner {
    position: absolute; left: 208px;
    width: 783px; height: 314px; overflow: hidden;
  }

  /* Memorial Day */
  .memorial {
    top: 236px;
    background:
      radial-gradient(circle at 88% 12%, var(--glow) 0%, var(--royal) 28%, var(--navy) 62%);
  }
  .memorial .flag-photo { position: absolute; left: 0; bottom: 0; width: 783px; height: 150px; }
  .memorial .candles-photo {
    position: absolute; right: 24px; top: 18px; width: 120px; height: 230px;
    border-radius: 10px;
    background: linear-gradient(180deg, #f4f6ff 0%, #cfd9f5 35%, var(--candle-gold) 62%, #c87518 100%);
  }
  .memorial .title {
    position: absolute; left: 36px; top: 38px;
    font: 700 44px/1 "Roboto Slab", serif; letter-spacing: 1px;
    background: linear-gradient(180deg, var(--title-light) 30%, var(--title-mid) 100%);
    -webkit-background-clip: text; background-clip: text; color: transparent;
  }
  .memorial .discount {
    position: absolute; left: 40px; top: 100px;
    color: var(--white); font: 400 74px/1 "Tinos", serif;
  }
  .memorial .discount b { font-weight: 700; }
  .memorial .scope {
    position: absolute; left: 158px; top: 172px;
    color: var(--white); font: 400 25px/1 "Tinos", serif;
  }
  .memorial .shipping-tag {
    position: absolute; left: 380px; top: 130px; width: 240px; height: 90px;
    transform: rotate(-30deg);
    background: var(--tag-red);
    clip-path: polygon(0 0, 88% 0, 100% 50%, 88% 100%, 0 100%);
    padding: 10px 34px 0 12px;
    color: var(--white); text-align: center;
  }
  .shipping-tag::after {
    content: ""; position: absolute; right: 18px; top: 40px;
    width: 10px; height: 10px; border-radius: 50%; background: #8a1e1c;
  }
  .shipping-tag .tag-lead { font: 700 19px/1.2 "Tinos", serif; letter-spacing: .5px; }
  .shipping-tag .tag-terms { font: 400 15px/1.25 "Arimo", sans-serif; }

  /* Father's Day */
  .fathers {
    top: 650px;
    background: linear-gradient(180deg, var(--sky-top) 0%, #b9dbf3 45%, var(--sky-bottom) 80%);
  }
  .fathers .sky-photo {
    position: absolute; inset: 0;
    background: radial-gradient(circle at 80% 10%, rgba(255,255,255,.85) 0%, rgba(255,255,255,0) 40%);
  }
  .fathers .shipping-band {
    position: absolute; left: 0; bottom: 0; width: 100%; height: 70px;
    background: linear-gradient(180deg, var(--band-light), var(--band-dark));
  }
  .fathers .shipping-line {
    position: absolute; left: 322px; bottom: 26px;
    color: var(--white); font: 400 19px/1 "Arimo", sans-serif; white-space: nowrap;
  }
  .fathers .shipping-line strong { font: 700 20px/1 "Tinos", serif; margin-right: 8px; letter-spacing: .5px; }
  .fathers .pennant { position: absolute; left: 50px; top: 30px; width: 260px; height: 284px; }
  .fathers .greeting { position: absolute; left: 62px; top: 52px; width: 236px; text-align: center; }
  .greeting .happy { color: var(--happy-red); font: 700 46px/1 "Dancing Script", cursive; }
  .greeting .who { color: var(--fathers-blue); font: 400 36px/1.1 "Arimo", sans-serif; margin-top: 6px; }
  .greeting .day { color: var(--day-green); font: 700 104px/0.95 "Roboto Condensed", sans-serif; }
  .fathers .offer { position: absolute; left: 310px; top: 26px; font-family: "Arimo", sans-serif; font-weight: 700; line-height: 1; }
  .offer span { display: block; paint-order: stroke fill; -webkit-text-stroke: 6px var(--white); }
  .offer .get { color: var(--text-blue); font-size: 56px; }
  .offer .amount { font-size: 70px; margin-top: 4px; color: var(--sale-pink); }
  .offer .range { color: var(--text-blue); font-size: 56px; margin-top: 4px; }
  .fathers .candle-photo {
    position: absolute; left: 645px; top: 84px; width: 100px; height: 118px;
    border-radius: 8px;
    background: linear-gradient(180deg, #f3e6de 0%, var(--wax-red) 25%, #6d0c08 100%);
  }
</style>
</head>
<body>
<main class="canvas">

  <section class="banner memorial" aria-label="Memorial Day sale banner">
    <svg class="flag-photo" viewBox="0 0 783 150" role="img" aria-label="Photo of a waving American flag">
      <defs>
        <linearGradient id="flagTone" x1="0" y1="0" x2="1" y2="0">
          <stop offset="0" stop-color="var(--flag-blue)"/>
          <stop offset=".35" stop-color="#3b4f9c"/>
          <stop offset=".55" stop-color="var(--flag-red)"/>
          <stop offset=".8" stop-color="#e7c9cc"/>
          <stop offset="1" stop-color="var(--flag-red)"/>
        </linearGradient>
      </defs>
      <path d="M0 80 C150 40 300 70 420 50 C540 30 640 40 783 0 L783 150 L0 150 Z" fill="url(#flagTone)"/>
    </svg>
    <div class="candles-photo" role="img" aria-label="Photo of two lit white candles in amber holders"></div>

    <h2 class="title">MEMORIAL DAY SALE</h2>
    <p class="discount"><b>25%</b> OFF</p>
    <p class="scope">Select Candles</p>

    <div class="shipping-tag">
      <p class="tag-lead">FREE SHIPPING</p>
      <p class="tag-terms">when you order<br>$50 or more.</p>
    </div>
  </section>

  <section class="banner fathers" aria-label="Father's Day sale banner">
    <div class="sky-photo" role="img" aria-label="Photo of a bright blue sky with soft clouds and sun rays"></div>
    <div class="shipping-band"></div>
    <p class="shipping-line"><strong>FREE SHIPPING</strong>when you order $75 or more.</p>

    <svg class="pennant" viewBox="0 0 260 284" aria-hidden="true">
      <path d="M4 4 L256 4 L256 220 L130 280 L4 220 Z" fill="var(--white)" stroke="var(--pennant-edge)" stroke-width="3"/>
    </svg>
    <div class="greeting">
      <p class="happy">Happy</p>
      <p class="who">FATHERS'S</p>
      <p class="day">DAY</p>
    </div>

    <p class="offer">
      <span class="get">Get</span>
      <span class="amount">30% OFF</span>
      <span class="range">all candles</span>
    </p>
    <div class="candle-photo" role="img" aria-label="Photo of a red candle in a glass jar"></div>
  </section>

</main>
</body>
</html>
```